Startup FinTech / Behavioural Science company needs website redesign

We are a startup company interested in redesigning our website. We have most of our content created already (viewable at www.tallowmint.example), but are interested in an upgraded look and feel. We are happy to adjust content as well based on design input. We will move hosting from brixelpad to hostvarra or similar hosting service, so portability of files is important to us. Our team will have the ability to make minor tweaks/content adjustments, but would look to engage with someone for more-comprehensive enhancements in the future.
Updates

Reason: Other business needs prevented me from providing timely feedback. I will work on feedback over the next two days but wanted to give additional time for design submissions and revisions.

Target Market(s)

Financial advisors in the US and UK, as well as potential end-users of the tools and potential investors

Industry/Entity Type

Information Technology

Coding

Coded - Design and coding required

Number of Pages Required

1 page

Font styles to use
Sans Serif

Requirements
Must have
• - Lighter, cleaner look and feel. We believe our current website is too heavy and "angular."
• - improved iconography to convey behavioural finance concepts (e.g., herd mentality, and illusion of control)
• - links to social media sites
• - integration with our brixelpad personality profile (viewable now at https://lenaobisk.formquill.example/to/qZ7mRt. Note: we will change this URL to tallowmint.formquill.example... as a part of the design process)
Nice to have
• - ability for us to add a tab/link to a blog in the future.
• - design that allows us to add additional
• - ability for us to add additional pages (e.g., results from our personality profiles, pages to customize sharing on social media)
• - simple ability to enter an email address to add to our mailing list/request more info
• - mobile-responsive design
Should not have
• - Should not have items like office directions and maps, since we are a virtual team.
• - Contact information (e.g., phone number) should be lower down the page vs. at the top
• - comments boxes or lengthy web forms. A simple name/email address is sufficient.

```html
<!DOCTYPE html>
<html lang="en">
<head>
<meta charset="utf-8">
<title>Tallowmint</title>
<link href="https://fonts.googleapis.com/css2?family=Montserrat:wght@400;500;600;700&family=Cinzel:wght@400&display=swap" rel="stylesheet">
<style>
:root{
  --purple:#8a2b9c;
  --purple-dark:#6f1f80;
  --ink:#222226;
  --grey:#555;
  --line:#b57fc4;
  --white:#fff;
  --footer:#3b3439;
}
*{box-sizing:border-box;margin:0;padding:0}
html,body{width:1200px;height:3666px;overflow:hidden}
body{position:relative;background:var(--white);font-family:"Montserrat",Arial,sans-serif;color:var(--ink)}
.abs{position:absolute}
.hero{left:0;top:0;width:1200px;height:640px;background:linear-gradient(135deg,#d8d6d3 0%,#8f98a6 35%,#48546a 60%,#c7c4c0 100%)}
.hero-shade{left:0;top:0;width:1200px;height:640px;background:rgba(20,25,40,.35)}
.nav-brand{left:0;top:30px;width:330px;height:82px;background:var(--white);clip-path:polygon(0 0,100% 0,88% 100%,0 100%)}
.nav-bar{left:290px;top:30px;width:910px;height:82px;background:var(--purple);clip-path:polygon(40px 0,100% 0,100% 100%,0 100%)}
.brand{font-weight:600;font-size:34px;color:var(--ink);display:flex;align-items:center;gap:10px;white-space:nowrap}
.brand .dot{width:16px;height:16px;border-radius:50%;background:var(--purple)}
.nav-links{left:440px;top:58px;display:flex;gap:28px;font-size:16px;color:var(--white);white-space:nowrap}
.nav-cta{left:968px;top:50px;width:198px;height:42px;background:var(--white);color:var(--ink);font-size:16px;display:flex;align-items:center;justify-content:center;border-radius:3px;white-space:nowrap}
.hero-kicker{left:0;width:1200px;top:246px;text-align:center;color:var(--white);font-size:28px;letter-spacing:12px;font-weight:600}
.hero-title{left:0;width:1200px;top:308px;text-align:center;color:var(--white);font-size:50px;font-weight:700}
.hero-title span{border-bottom:4px solid var(--white);padding-bottom:2px}
.hero-tag{left:380px;top:410px;width:440px;height:48px;background:var(--white);border:3px solid var(--purple);color:var(--purple);font-family:"Cinzel",Georgia,serif;font-size:21px;letter-spacing:3px;display:flex;align-items:center;justify-content:center;white-space:nowrap;overflow:hidden}
.btn{background:var(--purple);color:var(--white);font-size:14px;font-weight:500;display:flex;align-items:center;justify-content:center;text-transform:uppercase;white-space:nowrap}
.heading{font-size:38px;font-weight:400;display:flex;align-items:center;gap:18px;color:#333;white-space:nowrap}
.heading::after{content:"";width:64px;height:2px;background:var(--line)}
.heading.center{left:0;width:1200px;justify-content:center;padding-left:82px}
.body-text{font-size:16px;line-height:36px;color:var(--ink)}
.why-item{width:260px;text-align:center;font-size:18px}
.why-item svg{display:block;margin:0 auto 32px}
.lead{left:0;width:1200px;top:1568px;text-align:center;font-size:40px;font-weight:500}
.subhead{font-size:22px;color:#333}
.card{width:257px;height:342px}
.card-cap{left:0;bottom:0;width:100%;height:112px;background:rgba(40,40,40,.82);color:#eee;font-size:18px;display:flex;align-items:center;justify-content:center;white-space:nowrap}
.team{height:298px;border:2px solid var(--ink);background:var(--white)}
.team-photo{top:0;width:257px;height:294px}
.team-name{font-size:14px;font-weight:700;text-transform:uppercase}
.team-role{font-size:11px;color:var(--purple);margin-top:6px;text-transform:uppercase}
.team-list{font-size:12px;line-height:23px;margin-top:20px}
.field{border:2px solid #999;border-radius:6px;font-size:18px;display:flex;align-items:center;padding-left:16px;color:var(--ink)}
.social{display:flex;gap:26px}
.social span{width:18px;height:18px;border-radius:50%;background:var(--purple)}
.footer-bar{left:0;top:3573px;width:1200px;height:93px;background:var(--footer);color:var(--white);font-size:18px;display:flex;align-items:center;justify-content:center}
.footer-bar i{font-style:normal;border-left:2px solid #ccc;margin-left:12px;padding-left:12px}
</style>
</head>
<body>

<header>
  <div class="abs hero" role="img" aria-label="Photo of a stressed man at a desk covered with papers and a laptop"></div>
  <div class="abs hero-shade"></div>
  <div class="abs nav-brand"></div>
  <div class="abs brand" style="left:54px;top:50px"><span class="dot"></span>tallowmint</div>
  <div class="abs nav-bar"></div>
  <nav class="abs nav-links"><span>The Problem</span><span>The Solution</span><span>Our Team</span><span>Take Profile</span></nav>
  <div class="abs nav-cta">Get an appointment</div>
  <div class="abs hero-kicker">MONEY DECISIONS</div>
  <div class="abs hero-title"><span>CAN STRESS YOU OUT</span></div>
  <div class="abs hero-tag">TALLOWMINT CAN HELP</div>
  <div class="abs btn" style="left:520px;top:525px;width:160px;height:32px">Know more</div>
</header>

<section class="problem">
  <h2 class="abs heading center" style="top:704px">THE PROBLEM</h2>
  <p class="abs body-text" style="left:83px;top:818px;width:460px">Lorem Ipsum is simply dummy text of the printing and typesetting industry. Lorem Ipsum has been the industry's standard dummy text ever since the 1500s, when an printer took a galley of type and scrambled it to make a type specimen book</p>
  <div class="abs btn" style="left:83px;top:1040px;width:162px;height:35px">Learn more</div>
  <div class="abs" style="left:623px;top:808px;width:542px;height:319px;background:linear-gradient(135deg,#8a6a48,#b89a78 50%,#5e4a38)" role="img" aria-label="Top view of a team working at a wooden table with laptops and charts"></div>
</section>

<section class="why">
  <h2 class="abs heading center" style="top:1198px">WHY ?</h2>
  <div class="abs why-item" style="left:73px;top:1307px">
    <svg width="90" height="100" viewBox="0 0 90 100" fill="none" stroke="#222" stroke-width="3"><path d="M45 22a22 22 0 0 0-13 40v10h26V62a22 22 0 0 0-13-40z"/><path d="M34 80h22M37 88h16"/><path d="M45 4v8M16 16l6 6M74 16l-6 6M6 42h8M84 42h-8"/></svg>
    Short Term Thinking</div>
  <div class="abs why-item" style="left:351px;top:1307px">
    <svg width="90" height="100" viewBox="0 0 90 100" fill="none" stroke="#8a2b9c" stroke-width="6" stroke-linecap="round"><circle cx="26" cy="14" r="7" fill="#8a2b9c" stroke="none"/><circle cx="66" cy="14" r="7" fill="#8a2b9c" stroke="none"/><path d="M26 28v32M26 60l-12 30M26 60l12 30M26 36l-14 18M26 36l14 18"/><path d="M66 28v32M66 60l-12 30M66 60l12 30M66 36l-14 18M66 36l14 18"/></svg>
    Herd mentality</div>
  <div class="abs why-item" style="left:620px;top:1307px">
    <svg width="90" height="100" viewBox="0 0 90 100" fill="none" stroke="#222" stroke-width="3"><path d="M33 10h24l-6 16H39z"/><path d="M39 26C18 40 12 60 14 78c2 12 12 16 31 16s29-4 31-16c2-18-4-38-25-52"/><text x="45" y="76" font-size="34" text-anchor="middle" fill="#222" stroke="none" font-family="Arial">$</text></svg>
    Gambler's Fallacy</div>
  <div class="abs why-item" style="left:882px;top:1307px">
    <svg width="90" height="100" viewBox="0 0 90 100" fill="none" stroke="#8a2b9c" stroke-width="3"><path d="M45 8l36 18v44L45 90 9 70V26z"/><path d="M9 26l36 18 36-18M45 44v46"/><path d="M21 32v44M33 38v46M57 38v46M69 32v44M9 41l36 18 36-18M9 56l36 18 36-18M21 20l36 18M33 14l36 18M69 20L33 38M57 14L21 32"/></svg>
    Illusion of control</div>
</section>

<section class="intro">
  <h2 class="abs lead">This is where Tallowmint comes in</h2>
  <h3 class="abs heading center subhead" style="top:1648px;font-size:22px">THE TALLOWMINT SOLUTION</h3>
  <div class="abs" style="left:51px;top:1765px;width:567px;height:328px;background:linear-gradient(120deg,#dfe4ea,#8d96a3 55%,#2f3542)" role="img" aria-label="Photo of two businessmen reviewing documents together"></div>
  <p class="abs body-text" style="left:667px;top:1790px;width:460px">Lorem Ipsum is simply dummy text of the printing and typesetting industry. Lorem Ipsum has been the industry's standard dummy text ever since the 1500s, when an unknown printer took a galley of type and scrambled it to make a type specimen book</p>
  <div class="abs btn" style="left:667px;top:2009px;width:162px;height:34px">Learn more</div>
</section>

<section class="steps">
  <h2 class="abs" style="left:0;width:1200px;top:2204px;text-align:center;font-size:38px;font-weight:500">THE TALLOWMINT SOLUTION</h2>
  <div class="abs card" style="left:56px;top:2295px;background:linear-gradient(160deg,#e9c9c6,#6f8bb0)" role="img" aria-label="Laptop showing a dashboard">
    <div class="abs card-cap">Take the profile</div></div>
  <div class="abs card" style="left:337px;top:2295px;background:linear-gradient(180deg,#f1c46a,#b9743a 55%,#2f2a26)" role="img" aria-label="Glasses held against a sunset over the sea">
    <div class="abs card-cap">Gain better insight</div></div>
  <div class="abs card" style="left:618px;top:2295px;background:linear-gradient(180deg,#f2f3f5,#9aa3ae 60%,#444c57)" role="img" aria-label="Business handshake">
    <div class="abs card-cap">Connect your accounts</div></div>
  <div class="abs card" style="left:904px;top:2295px;background:linear-gradient(160deg,#dfe7f0,#9db4c8 60%,#55626f)" role="img" aria-label="Hands reviewing charts on paper">
    <div class="abs card-cap">Check your progress</div></div>
</section>

<section class="team-section">
  <h2 class="abs heading center" style="top:2704px;font-weight:500">ABOUT OUR TEAM</h2>
  <div class="abs team" style="left:90px;top:2813px;width:499px">
    <div class="abs team-photo" style="left:0;background:linear-gradient(180deg,#7fa6c9,#2b3d55)" role="img" aria-label="Portrait of the CEO in a suit"></div>
    <div class="abs" style="left:292px;top:38px;width:200px">
      <div class="team-name">Lena Obisk, CFA</div>
      <div class="team-role">CEO / Head of "Fin"</div>
      <div class="team-list">FinTech Veteran<br>Investment Portfolio<br>Harrowgate Business School<br>Westbrook Tech University<br>Profile</div>
    </div>
    <div class="abs btn" style="left:330px;top:240px;width:160px;height:32px;font-size:13px">Learn more</div>
  </div>
  <div class="abs team" style="left:665px;top:2813px;width:489px">
    <div class="abs" style="left:36px;top:38px;width:200px">
      <div class="team-name">Tomas Redvale</div>
      <div class="team-role">CTO / Head of "Tech"</div>
      <div class="team-list">Data Science Expert<br>Predictive Analytics Solution<br>Coldwater University<br>University of Linmoor<br>Profile</div>
    </div>
    <div class="abs btn" style="left:28px;top:240px;width:160px;height:32px;font-size:13px">Learn more</div>
    <div class="abs team-photo" style="left:230px;width:255px;background:linear-gradient(180deg,#4a4a4a,#1f1f1f)" role="img" aria-label="Portrait of the CTO in a grey jacket"></div>
  </div>
</section>

<footer>
  <div class="abs brand" style="left:64px;top:3206px;font-size:30px"><span class="dot"></span>tallowmint</div>
  <div class="abs" style="left:40px;top:3290px;width:230px;text-align:center;font-size:17px;line-height:34px">Email:<br>info@tallowmint.example</div>
  <div class="abs social" style="left:86px;top:3480px" aria-label="Social media links"><span></span><span></span><span></span></div>
  <h2 class="abs heading" style="left:335px;top:3206px;font-size:38px">Subscribe To Our Newsletter</h2>
  <div class="abs" style="left:345px;top:3278px;font-size:22px">Contact us</div>
  <div class="abs field" style="left:342px;top:3331px;width:203px;height:47px">Name</div>
  <div class="abs field" style="left:342px;top:3392px;width:435px;height:47px">E-mail</div>
  <div class="abs btn" style="left:342px;top:3473px;width:183px;height:37px;font-size:17px">Submit</div>
  <div class="abs footer-bar">©2017 Tallowmint&amp;Quillby<i>All Right Reserved</i></div>
</footer>

</body>
</html>
```